Web design for a dental and eye clinic

We need a web design for a dental and eye clinic ( with medical laboratory services) with two branches in Lagos Nigeria. The ultimate aim is to attract more patronage. The design should have links to social media and should have provision for appointments and enquiries. Blue should be part of the colours

Name of facility. VORANTECLINICS Added Saturday, May 27, 2017

Target Market(s)

Lagos. Nigeria

Industry/Entity Type

Health Care

Number of Pages Required

3 page

Font styles to use
Sans Serif

Colors
85cae6
cadf82

Requirements
Must have
• a projection of the professioal services rendered
Nice to have
• portal for enquiries and appointments
• Link to our facebook, twitter and instagram

```html
<!DOCTYPE html>
<html lang="en">
<head>
<meta charset="utf-8">
<title>Vorante Dental &amp; Eye Clinic</title>
<link href="https://fonts.googleapis.com/css2?family=Open+Sans:wght@400;600;700&display=swap" rel="stylesheet">
<style>
:root{
  --blue:#85cae6;
  --blue-dark:#6bb8d8;
  --green:#cadf82;
  --ink:#333333;
  --muted:#777777;
  --line:#d9d9d9;
  --panel:#efefef;
  --footer:#353535;
  --white:#ffffff;
  --social:#4a7bb5;
}
*{box-sizing:border-box;margin:0;padding:0}
html,body{width:1200px;height:2459px;overflow:hidden}
body{font-family:"Open Sans",Arial,sans-serif;color:var(--ink);background:var(--white);position:relative}
.wrap{width:936px;margin:0 auto;position:relative}

/* header */
.site-header{height:113px}
.site-header .wrap{height:113px;display:flex;align-items:center;justify-content:space-between}
.brand-name{font-size:42px;font-weight:700;color:var(--blue);line-height:1;letter-spacing:1px}
.brand-tag{font-size:16px;color:var(--muted);margin-top:2px}
.header-info{display:flex;gap:34px}
.info-item{display:flex;align-items:center;gap:8px;text-align:right;white-space:nowrap}
.info-item small{display:block;font-size:13px;color:var(--muted)}
.info-item strong{display:block;font-size:17px;font-weight:600;color:#555}
.dot{width:30px;height:30px;border-radius:50%;background:var(--green);display:flex;align-items:center;justify-content:center;flex:none}

/* nav */
.main-nav{background:var(--blue);height:41px}
.main-nav ul{list-style:none;display:flex;height:41px;width:936px;margin:0 auto}
.main-nav li{color:var(--white);font-size:13px;font-weight:600;line-height:41px;padding:0 22px}
.main-nav li.active{background:var(--blue-dark)}
.main-nav li.enquiries{margin-left:auto;background:#666;padding:0 25px}

/* hero */
.hero{height:461px;display:flex;position:relative}
.hero-panel{flex:1;position:relative;overflow:hidden}
.hero-media{position:absolute;inset:0}
.hero-dental .hero-media{background:linear-gradient(120deg,#c9b79c 0%,#e5ddd3 40%,#9cc9dc 80%,#bcdbe8 100%)}
.hero-eye .hero-media{background:linear-gradient(120deg,#d8dde2 0%,#f2f2f2 45%,#c7ccd3 100%)}
.hero-title{position:absolute;text-align:center;color:var(--white);font-size:46px;font-weight:700;letter-spacing:1px;line-height:60px}
.hero-title.dental{left:215px;width:300px;top:296px}
.hero-title.eye{left:683px;width:300px;top:349px}
.hero-btn{position:absolute;left:254px;top:359px;width:222px;height:42px;background:#222;color:var(--white);font-size:16px;font-weight:600;display:flex;align-items:center;justify-content:center}
.hero-curve{position:absolute;bottom:0;width:170px;height:42px}
.hero-arrow{position:absolute;left:1174px;top:212px;width:26px;height:36px;background:rgba(80,80,80,.6);display:flex;align-items:center;justify-content:center}

/* services */
.services{padding-top:68px;height:388px}
.service-grid{display:flex;gap:21px}
.service{width:218px;text-align:center}
.service-img{height:159px}
.service-name{margin-top:10px;font-size:17px;color:var(--blue)}
.btn-blue{display:flex;align-items:center;justify-content:center;background:var(--blue);color:var(--white);font-weight:600;font-size:16px;width:128px;height:44px;margin:32px auto 0}

/* welcome */
.welcome{background:var(--panel);height:275px;text-align:center;padding-top:74px}
.section-title{font-size:34px;font-weight:700;color:#3a3a3a}
.welcome p{font-size:11px;color:var(--muted);line-height:20px;margin-top:10px}

/* blog */
.blog{height:587px;padding-top:73px}
.blog-head{display:flex;justify-content:space-between;align-items:center;border-bottom:1px solid var(--line);padding-bottom:12px}
.blog-head h2{font-size:32px;font-weight:700;color:var(--blue)}
.blog-grid{display:flex;gap:24px;margin-top:24px}
.post{width:296px}
.post-img{height:192px}
.post h3{font-size:16px;font-weight:400;line-height:22px;margin-top:14px;color:#222}
.post p{font-size:11px;line-height:18px;color:var(--muted);margin-top:8px}
.post time{display:block;font-size:11px;color:var(--muted);margin-top:14px}

/* appointment */
.booking{background:var(--panel);height:384px;padding-top:74px;text-align:center}
.form-grid{display:grid;grid-template-columns:repeat(4,1fr);gap:24px 22px;margin-top:30px;text-align:left}
.field{height:40px;background:var(--white);border:1px solid var(--line);font-size:11px;color:#888;padding:0 13px;display:flex;align-items:center;justify-content:space-between}
.field.wide{grid-column:span 2}
.btn-dark{display:inline-flex;align-items:center;justify-content:center;background:#333;color:var(--white);font-size:12px;font-weight:600;width:80px;height:37px;margin-top:26px}

/* contact strip */
.contact-strip{height:113px}
.contact-strip .wrap{height:113px;display:flex;align-items:center}
.contact-item{display:flex;align-items:center;gap:10px;white-space:nowrap}
.contact-item.location{width:394px}
.contact-item.phone{width:210px}
.contact-item small{display:block;font-size:13px;color:var(--muted)}
.contact-item strong{display:block;font-size:17px;font-weight:600;color:#555}
.social{margin-left:auto;display:flex;gap:10px}
.social span{width:33px;height:33px;border:1px solid var(--social);border-radius:50%;display:block}

/* footer */
.site-footer{background:var(--footer);height:97px;text-align:center;color:#ddd;padding-top:24px}
.footer-links{font-size:12px}
.footer-links span{margin:0 7px;color:#aaa}
.copyright{font-size:11px;margin-top:12px;color:#ccc}
</style>
</head>
<body>

<header class="site-header">
  <div class="wrap">
    <div class="brand">
      <div class="brand-name">VORANTE</div>
      <div class="brand-tag">Dental &amp; Eye Clinic</div>
    </div>
    <div class="header-info">
      <div class="info-item">
        <div><small>Our Location</small><strong>Kolade Crescent, Lagos, Ikeja, Nigeria</strong></div>
        <span class="dot"><svg width="14" height="16" viewBox="0 0 14 16"><path d="M7 0a6 6 0 0 0-6 6c0 4.5 6 10 6 10s6-5.5 6-10a6 6 0 0 0-6-6zm0 8.5A2.5 2.5 0 1 1 7 3.5a2.5 2.5 0 0 1 0 5z" fill="#fff"/></svg></span>
      </div>
      <div class="info-item">
        <div><small>Call us on</small><strong>08014528813</strong></div>
        <span class="dot"><svg width="14" height="14" viewBox="0 0 24 24"><path d="M6.6 10.8a15 15 0 0 0 6.6 6.6l2.2-2.2a1 1 0 0 1 1-.25 11.4 11.4 0 0 0 3.6.6 1 1 0 0 1 1 1V20a1 1 0 0 1-1 1A17 17 0 0 1 3 4a1 1 0 0 1 1-1h3.5a1 1 0 0 1 1 1c0 1.25.2 2.45.6 3.6a1 1 0 0 1-.25 1z" fill="#fff"/></svg></span>
      </div>
    </div>
  </div>
</header>

<nav class="main-nav">
  <ul>
    <li class="active">HOME</li><li>ABOUT US</li><li>DENTAL</li><li>EYE</li><li>PRODUCTS</li><li>BLOG</li><li>TESTIMONIALS</li><li>CONTACT US</li><li class="enquiries">ENQUIRIES</li>
  </ul>
</nav>

<section class="hero">
  <div class="hero-panel hero-dental">
    <div class="hero-media" role="img" aria-label="Smiling patient seated in a dental chair"></div>
  </div>
  <div class="hero-panel hero-eye">
    <div class="hero-media" role="img" aria-label="Optometrist holding up a pair of glasses"></div>
  </div>
  <div class="hero-title dental">DENTAL</div>
  <div class="hero-btn">BOOK AN APPOINTMENT</div>
  <div class="hero-title eye">EYE</div>
  <svg class="hero-curve" style="left:280px" viewBox="0 0 170 42" aria-hidden="true"><path d="M0 42C40 42 45 2 85 2s45 40 85 40z" fill="#fff"/><path d="M79 14c-3 0-5 2-5 5 0 4 2 5 2 9 0 3 1 5 2 5s1-4 3-4 2 4 3 4 2-2 2-5c0-4 2-5 2-9 0-3-2-5-5-5-1 0-2 1-2 1s-1-1-2-1z" fill="none" stroke="#85cae6" stroke-width="1.3"/></svg>
  <svg class="hero-curve" style="left:748px" viewBox="0 0 170 42" aria-hidden="true"><path d="M0 42C40 42 45 2 85 2s45 40 85 40z" fill="#fff"/><path d="M70 24c8-10 22-10 30 0-8 10-22 10-30 0z" fill="#555"/><circle cx="85" cy="24" r="5" fill="#fff"/><circle cx="85" cy="24" r="2.5" fill="#555"/></svg>
  <div class="hero-arrow"><svg width="8" height="12" viewBox="0 0 8 12"><path d="M1 1l5 5-5 5" stroke="#fff" stroke-width="2" fill="none"/></svg></div>
</section>

<section class="services">
  <div class="wrap">
    <div class="service-grid">
      <div class="service"><div class="service-img" role="img" aria-label="Dentist examining a patient" style="background:linear-gradient(135deg,#5a3d30,#a99c94)"></div><div class="service-name">General Dentistry</div></div>
      <div class="service"><div class="service-img" role="img" aria-label="Dental mirror inside an open smile" style="background:linear-gradient(135deg,#c9765e,#f0e5e0)"></div><div class="service-name">Orthodontics</div></div>
      <div class="service"><div class="service-img" role="img" aria-label="Model of a dental implant between teeth" style="background:linear-gradient(135deg,#f1b9a8,#e7e1d8)"></div><div class="service-name">Tootth Replacement</div></div>
      <div class="service"><div class="service-img" role="img" aria-label="Smile before and after whitening" style="background:linear-gradient(135deg,#c8624c,#f4ece8)"></div><div class="service-name">Cosmetic Dentistry</div></div>
    </div>
    <div class="btn-blue">ENQUIRIES</div>
  </div>
</section>

<section class="welcome">
  <div class="wrap">
    <h1 class="section-title">WELCOME TO VORANTE DENTAL &amp; EYE CLINIC</h1>
    <p>Our two Lagos branches bring dental care, eye care and medical laboratory services together under one roof. Our friendly team of dentists, optometrists and lab scientists works with modern equipment to give every patient clear advice and gentle treatment. From routine check-ups and cleaning to fitting glasses, implants and full eye tests, we look after the whole family. Book a visit today at either branch, ask us any question through our enquiries page, and let us help you see and smile with confidence every day.</p>
  </div>
</section>

<section class="blog">
  <div class="wrap">
    <div class="blog-head">
      <h2>BLOG</h2>
      <svg width="58" height="14" viewBox="0 0 58 14" aria-hidden="true"><path d="M2 7h22M2 7l5-4M2 7l5 4M34 7h22M56 7l-5-4M56 7l-5 4" stroke="#555" stroke-width="2.2" fill="none"/></svg>
    </div>
    <div class="blog-grid">
      <article class="post"><div class="post-img" role="img" aria-label="Man brushing his teeth" style="background:linear-gradient(135deg,#7a5444,#e6e2df)"></div><h3>Pellentesque dolor lectus, consequat sit amet luctus in, bibendum in ante</h3><p>Brushing twice a day keeps your gums healthy. Learn simple habits that protect your teeth and keep your smile bright between visits.</p><time>27 May, 2017</time></article>
      <article class="post"><div class="post-img" role="img" aria-label="Dental handpieces on a tray" style="background:linear-gradient(135deg,#dfe3e6,#9fa8ae)"></div><h3>Pellentesque dolor lectus, consequat sit amet luctus in, bibendum in ante</h3><p>Curious about the tools in our clinic? We explain what each instrument does so your next dental visit feels calm and easy.</p><time>27 May, 2017</time></article>
      <article class="post"><div class="post-img" role="img" aria-label="Child covering one eye beside an eye chart" style="background:linear-gradient(135deg,#6a4a3c,#e9eef2)"></div><h3>Pellentesque dolor lectus, consequat sit amet luctus in, bibendum in ante</h3><p>Children should have regular eye tests. Find out which signs show your child may need glasses and when to book a check.</p><time>27 May, 2017</time></article>
    </div>
  </div>
</section>

<section class="booking">
  <div class="wrap">
    <h2 class="section-title">BOOK AN APPOINTMENT</h2>
    <div class="form-grid">
      <div class="field">Name</div>
      <div class="field">Email</div>
      <div class="field">Phone</div>
      <div class="field">City</div>
      <div class="field">Treatment For <svg width="10" height="6" viewBox="0 0 10 6"><path d="M1 1l4 4 4-4" stroke="#666" fill="none"/></svg></div>
      <div class="field">Date <svg width="13" height="13" viewBox="0 0 13 13"><rect x="1" y="2" width="11" height="10" fill="none" stroke="#777"/><path d="M1 5h11M4 1v2M9 1v2" stroke="#777"/></svg></div>
      <div class="field wide">Message</div>
    </div>
    <div class="btn-dark">SUBMIT</div>
  </div>
</section>

<section class="contact-strip">
  <div class="wrap">
    <div class="contact-item location"><span class="dot"><svg width="14" height="16" viewBox="0 0 14 16"><path d="M7 0a6 6 0 0 0-6 6c0 4.5 6 10 6 10s6-5.5 6-10a6 6 0 0 0-6-6zm0 8.5A2.5 2.5 0 1 1 7 3.5a2.5 2.5 0 0 1 0 5z" fill="#fff"/></svg></span><div><small>Our Location</small><strong>Kolade Crescent, Lagos, Ikeja, Nigeria</strong></div></div>
    <div class="contact-item phone"><span class="dot"><svg width="14" height="14" viewBox="0 0 24 24"><path d="M6.6 10.8a15 15 0 0 0 6.6 6.6l2.2-2.2a1 1 0 0 1 1-.25 11.4 11.4 0 0 0 3.6.6 1 1 0 0 1 1 1V20a1 1 0 0 1-1 1A17 17 0 0 1 3 4a1 1 0 0 1 1-1h3.5a1 1 0 0 1 1 1c0 1.25.2 2.45.6 3.6a1 1 0 0 1-.25 1z" fill="#fff"/></svg></span><div><small>Call us on</small><strong>08014528813</strong></div></div>
    <div class="contact-item email"><span class="dot"><svg width="14" height="11" viewBox="0 0 14 11"><rect x="0.5" y="0.5" width="13" height="10" fill="none" stroke="#fff"/><path d="M1 1l6 5 6-5" stroke="#fff" fill="none"/></svg></span><div><small>Email</small><strong>info@vorante.com</strong></div></div>
    <div class="social" aria-label="Social media links"><span aria-label="Social link one"></span><span aria-label="Social link two"></span><span aria-label="Social link three"></span></div>
  </div>
</section>

<footer class="site-footer">
  <div class="footer-links">Home<span>|</span>About Us<span>|</span>Dental<span>|</span>Eye<span>|</span>Products<span>|</span>Blog<span>|</span>Testimonials<span>|</span>Contact Us<span>|</span>Enquiries<span>|</span>Book an Appointment</div>
  <div class="copyright">Copyright &copy; 2017 Vorante Dental &amp; Eye Clinic. &nbsp;All rights reserved.</div>
</footer>

</body>
</html>
```